Luminously Grounded Vitality

We want to design a business card that is modern and appealing for an innovative psychedelic telemedicine company that provides at-home ketamine-assisted therapy along with wellness, longevity, and anti-aging medicines. We want to use our deep purple and white plus other colors you can find on our website. We don't have any strict brand guidelines yet so feel free to get creative. We want a very professional, but technology first modern design that will instill trust, peace, calm, but also be attractive to investors in the healthcare and SaaS space.

```html
<!DOCTYPE html>
<html lang="en">
<head>
<meta charset="utf-8">
<title>Luminously Grounded Vitality — Business Card</title>
<link href="https://fonts.googleapis.com/css2?family=Lato:wght@300;400;700;900&display=swap" rel="stylesheet">
<style>
  :root {
    --plum-deep: #2a1a42;
    --lavender: #7d62b0;
    --orchid: #b06fa4;
    --paper: #ffffff;
    --backdrop: #ece9f0;
  }
  * { margin: 0; padding: 0; box-sizing: border-box; }
  html, body { width: 1200px; height: 977px; overflow: hidden; }
  body {
    background: var(--backdrop);
    font-family: "Lato", sans-serif;
    position: relative;
  }
  .card {
    position: absolute;
    width: 560px;
    height: 320px;
    border-radius: 22px;
    overflow: hidden;
    box-shadow: 0 10px 28px rgba(42, 26, 66, 0.22);
  }
  .card-back {
    left: 60px; top: 110px;
    background: var(--plum-deep);
    display: flex; align-items: center; justify-content: center; gap: 18px;
  }
  .brand-dot {
    width: 34px; height: 34px; border-radius: 50%;
    background: var(--lavender);
  }
  .brand-name {
    color: var(--orchid);
    font-weight: 300;
    font-size: 34px;
    letter-spacing: 0.5px;
  }
  .card-front {
    left: 580px; top: 540px;
    background: var(--paper);
  }
  .card-front svg.wave { position: absolute; inset: 0; }
  .front-mark {
    position: absolute; left: 110px; top: 105px;
    width: 110px; height: 110px; border-radius: 50%;
    background: var(--lavender);
  }
  .holder {
    position: absolute; right: 34px; top: 24px; text-align: right;
  }
  .holder-name {
    color: var(--lavender); font-weight: 900; font-size: 22px; line-height: 26px; letter-spacing: 0.3px;
  }
  .holder-role {
    color: var(--orchid); font-weight: 400; font-size: 13px; line-height: 16px; margin-top: 1px;
  }
  .contact {
    position: absolute; right: 24px; top: 165px;
    list-style: none; text-align: right;
    color: var(--paper); font-size: 10.5px; line-height: 16px;
  }
  .contact li { display: flex; justify-content: flex-end; align-items: center; gap: 8px; white-space: nowrap; }
  .contact .icon { width: 10px; height: 10px; flex: none; }
  .contact .no-icon { width: 10px; flex: none; }
</style>
</head>
<body>
  <section class="card card-back">
    <span class="brand-dot"></span>
    <span class="brand-name">Luminously Grounded Vitality</span>
  </section>

  <section class="card card-front">
    <svg class="wave" viewBox="0 0 560 320" width="560" height="320" aria-hidden="true">
      <path d="M560,106 C420,102 370,130 340,190 C310,250 280,288 160,290 C100,291 50,288 0,284 L0,320 L560,320 Z" fill="var(--plum-deep)"/>
      <path d="M560,92 C414,88 358,118 328,180" fill="none" stroke="var(--lavender)" stroke-width="6"/>
      <path d="M322,196 C292,254 262,280 160,282 C100,283 50,280 0,276" fill="none" stroke="var(--orchid)" stroke-width="6"/>
    </svg>
    <span class="front-mark"></span>
    <div class="holder">
      <p class="holder-name">DANIEL REYES</p>
      <p class="holder-role">Founder &amp; CEO</p>
    </div>
    <ul class="contact">
      <li>+1 833-555-0142
        <svg class="icon" viewBox="0 0 10 10"><path d="M2 1 L4 3 L3 4 C4 6 5 7 6 7 L7 6 L9 8 L8 9 C4 9 1 6 1 2 Z" fill="var(--orchid)"/></svg></li>
      <li>hello@luminouslyvitality.com
        <svg class="icon" viewBox="0 0 10 10"><rect x="1" y="2.5" width="8" height="5.5" fill="var(--orchid)"/><path d="M1 2.5 L5 6 L9 2.5" fill="none" stroke="var(--plum-deep)" stroke-width="0.8"/></svg></li>
      <li>www.luminouslyvitality.com
        <svg class="icon" viewBox="0 0 10 10"><circle cx="5" cy="5" r="4" fill="var(--orchid)"/></svg></li>
      <li>245 Maple Avenue, Suite 900
        <svg class="icon" viewBox="0 0 10 10"><path d="M5 10 C2 6 2 5 2 4 A3 3 0 0 1 8 4 C8 5 8 6 5 10 Z" fill="var(--orchid)"/><circle cx="5" cy="4" r="1.1" fill="var(--plum-deep)"/></svg></li>
      <li>Boulder, CO, US, 80302<span class="no-icon"></span></li>
    </ul>
  </section>
</body>
</html>
```